Hot-air ballooning company needs a DL-size flyer

Skylark Aerial Tours is a hot-air ballooning company which flies passengers in the King Valley, Victoria, Australia.
We need a 2-sided DL-size flyer which promotes our hot-air balloon flights and packages.
Most of our customers are couples, and we want the flyer design to communicate safety, adventure, and romance.
The flyer should make the best use of our images which we provide, and we've also included a document with the text for the flyer.
Updates

2 days is not long enough to gather designs, the brief never asked me what my deadline should be.

Target Market(s)

Couples, buyers are majority female, between the ages of 20-60

Industry/Entity Type

Tourism

Font styles to use
Sans Serif

Colors

Designer to choose colors to be used in the design.

Requirements
Must have
• Communicate safety, adventure, and romance
• Use images
Nice to have
• There is a lot of text, it would be great if you could make it look like as little text as possible
Should not have
• No childish designs

```html
<!DOCTYPE html>
<html lang="en">
<head>
<meta charset="utf-8">
<title>Skylark Aerial Tours – Your Flight</title>
<link href="https://fonts.googleapis.com/css2?family=Jost:ital,wght@0,300;0,400;0,500;1,300&display=swap" rel="stylesheet">
<style>
  :root {
    --brand-red: #d7262e;
    --ink: #2e2e2e;
    --rule: #9a9a9a;
    --paper: #ffffff;
  }
  * { box-sizing: border-box; margin: 0; padding: 0; }
  html, body { width: 1200px; height: 566px; overflow: hidden; background: var(--paper); }
  body { font-family: "Jost", "Helvetica Neue", Arial, sans-serif; color: var(--ink); }
  .flyer { position: relative; width: 1200px; height: 566px; }

  .flight-details { position: absolute; left: 48px; top: 48px; width: 740px; }
  .flight-details h2 {
    font-weight: 400; font-size: 24px; letter-spacing: 0.3px;
    color: var(--brand-red); line-height: 1; margin-bottom: 14px;
  }
  .flight-details ul { list-style: none; }
  .flight-details li {
    position: relative; padding-left: 25px;
    font-size: 15.6px; font-weight: 300; line-height: 19.4px;
  }
  .flight-details li::before {
    content: ""; position: absolute; left: 2px; top: 7px;
    width: 5px; height: 5px; border-radius: 50%; background: var(--ink);
  }

  .column-rule { position: absolute; left: 827px; top: 40px; width: 1px; height: 262px; background: var(--rule); }

  .contact { position: absolute; left: 864px; top: 88px; font-size: 15.6px; font-weight: 300; line-height: 19.4px; }
  .contact .lead { color: var(--brand-red); font-weight: 500; }
  .contact .handle { color: var(--brand-red); font-weight: 500; }
  .contact .social { margin-top: 19.4px; }

  .photo-strip { position: absolute; left: 0; top: 336px; width: 1200px; height: 163px; display: flex; }
  .photo { flex: 1; height: 100%; }
  .photo--sunrise-launch { background: linear-gradient(180deg, #4f86c2 0%, #8db3d8 62%, #7a7a62 80%, #4d4a3a 100%); }
  .photo--basket-river { background: linear-gradient(160deg, #bfc4c2 0%, #c69a45 40%, #7b8a4d 65%, #5c6f42 100%); }
  .photo--night-inflation { background: linear-gradient(180deg, #2f3b55 0%, #c4552a 40%, #f2a23a 60%, #3a3536 100%); }
  .photo--misty-valley { background: linear-gradient(180deg, #3b78b7 0%, #86b1d6 55%, #c9d3dc 75%, #6e7266 100%); }

  .certificate {
    position: absolute; left: 0; top: 515px; width: 1200px; text-align: center;
    font-size: 11.2px; font-style: italic; font-weight: 300;
  }
</style>
</head>
<body>
<main class="flyer">
  <section class="flight-details">
    <h2>YOUR FLIGHT</h2>
    <ul>
      <li>One-hour sunrise balloon flight in the spectacular King Valley region in North East Victoria</li>
      <li>Delicious champagne breakfast after the flight (recommended option)</li>
      <li>Informative details throughout your experience with our locally based expert crew</li>
      <li>The opportunity to be involved in the inflation and deflation process should you wish</li>
      <li>Safe, friendly and professional</li>
      <li>The flight lasts approximately 1 hour</li>
      <li>The entire experience takes about 3-4 hours</li>
      <li>Suitable from age 7 to 97</li>
      <li>Gift Vouchers are also available</li>
      <li>Contact us for exclusive flight options at your custom location</li>
    </ul>
  </section>

  <div class="column-rule"></div>

  <aside class="contact">
    <p class="lead">For bookings or more information:</p>
    <p>www.skylarkaerialtours.com.au</p>
    <p>flights@skylarkaerialtours.com.au</p>
    <p>or call our friendly team on 1300 555 019</p>
    <p class="social">Find us also on</p>
    <p>FaceSpace, Photogram and TravelNotes</p>
    <p class="handle">@skylarkaerialtours</p>
  </aside>

  <div class="photo-strip">
    <div class="photo photo--sunrise-launch" role="img" aria-label="Colourful hot-air balloons rising over a country town in a clear blue morning sky"></div>
    <div class="photo photo--basket-river" role="img" aria-label="Passengers in a balloon basket drifting low over a river lined with autumn trees"></div>
    <div class="photo photo--night-inflation" role="img" aria-label="Balloons glowing with burner flames during pre-dawn inflation as spectators watch"></div>
    <div class="photo photo--misty-valley" role="img" aria-label="Patterned hot-air balloons floating above a misty valley with distant hills"></div>
  </div>

  <p class="certificate">Skylark Aerial Tours operates under Air Operator's Certificate C100482-17 issued by the National Air Safety Office</p>
</main>
</body>
</html>
```